managed network and cloud support

Let’s design a business card that will be as simple and bold at the same time. Name, email address, website & phone number.

Target Market(s)

Small to Medium Size Business

Industry/Entity Type

It Professional

Contact Information for Business Card

Name, email, website, phone numbers

Font styles to use
Sans Serif

Colors
ec1f27
f04a50
dddddd
919191
000000
ffffff

Requirements
Must have
• Clean simple look using my existing logo. I just need to the basic contact information on this card.
Nice to have
• Im considering the square size card versus the standard size business card.
Should not have
• No Mailing Address, no list of services.

```html
<!DOCTYPE html>
<html lang="en">
<head>
<meta charset="utf-8">
<title>Corvid Systems business card</title>
<link rel="stylesheet" href="https://fonts.googleapis.com/css2?family=Montserrat:wght@400;500;600;700&display=swap">
<style>
  :root {
    --red: #ec1f27;
    --red-soft: #f04a50;
    --light: #dddddd;
    --mid: #919191;
    --black: #000000;
    --white: #ffffff;
    --stage: #2b2b2b;
  }
  * { box-sizing: border-box; margin: 0; padding: 0; }
  html, body { width: 1200px; height: 880px; overflow: hidden; }
  body {
    background: var(--stage);
    font-family: "Montserrat", sans-serif;
    position: relative;
  }
  .card {
    position: absolute;
    width: 560px;
    height: 320px;
    overflow: hidden;
    box-shadow: 0 14px 30px rgba(0,0,0,0.5);
  }
  .card-front { left: 70px; top: 70px; background: var(--black); }
  .card-back { left: 570px; top: 490px; background: var(--white); }

  .brand { display: flex; align-items: center; gap: 10px; }
  .brand-dot {
    width: 12px; height: 12px; border-radius: 50%;
    background: var(--red);
    flex: none;
  }
  .brand-name {
    font-weight: 600;
    font-size: 30px;
    letter-spacing: 0.5px;
    line-height: 1;
    white-space: nowrap;
  }
  .brand-tagline {
    font-size: 11px;
    letter-spacing: 1px;
    margin-top: 6px;
    margin-left: 22px;
    white-space: nowrap;
  }

  .card-front .brand-block {
    position: absolute; left: 0; right: 0; top: 118px;
    display: flex; flex-direction: column; align-items: center;
  }
  .card-front .brand-name { color: var(--white); }
  .card-front .brand-tagline { color: var(--light); margin-left: 0; }
  .front-web {
    position: absolute; left: 0; right: 0; top: 232px;
    text-align: center; font-size: 12px; color: var(--white);
  }
  .front-web .accent { color: var(--red); }

  .card-back .brand-block {
    position: absolute; left: 34px; top: 118px;
  }
  .card-back .brand-name { color: var(--black); font-size: 24px; }
  .card-back .brand-tagline { color: var(--mid); font-size: 9px; letter-spacing: 0.6px; }

  .divider {
    position: absolute; left: 300px; top: 50px;
    width: 1px; height: 120px; background: var(--red);
  }
  .contact { position: absolute; left: 322px; top: 46px; }
  .person-name { font-weight: 700; font-size: 21px; color: var(--black); }
  .person-role { font-size: 13px; color: var(--red); margin-top: 1px; }
  .contact-list { list-style: none; margin-top: 14px; }
  .contact-list li {
    display: flex; align-items: center; gap: 8px;
    font-size: 12px; color: var(--black); margin-bottom: 5px;
  }
  .contact-icon { width: 16px; height: 16px; flex: none; }

  .wave { position: absolute; left: 0; bottom: 0; width: 560px; height: 160px; }
</style>
</head>
<body>

<section class="card card-front">
  <div class="brand-block">
    <div class="brand">
      <span class="brand-dot"></span>
      <span class="brand-name">corvid systems</span>
    </div>
    <p class="brand-tagline">managed network and cloud support</p>
  </div>
  <p class="front-web">www.<span class="accent">corvidsystems</span>.com</p>
</section>

<section class="card card-back">
  <div class="brand-block">
    <div class="brand">
      <span class="brand-dot"></span>
      <span class="brand-name">corvid systems</span>
    </div>
    <p class="brand-tagline">managed network and cloud support</p>
  </div>

  <div class="divider"></div>

  <div class="contact">
    <p class="person-name">Daniel Reyes</p>
    <p class="person-role">Founder</p>
    <ul class="contact-list">
      <li>
        <svg class="contact-icon" viewBox="0 0 16 16"><circle cx="8" cy="8" r="7.5" fill="none" stroke="var(--red)"/><path d="M5 4.5c.6-.4 1.2 0 1.5.7l.5 1.2-.8.7c.4.9 1 1.6 1.9 2l.7-.8 1.2.5c.7.3 1 .9.6 1.5-.6.9-1.6 1-2.6.5C6.3 10 5 8.6 4.5 7c-.3-1 0-2 .5-2.5z" fill="var(--red)"/></svg>
        (555) 014-2270
      </li>
      <li>
        <svg class="contact-icon" viewBox="0 0 16 16"><circle cx="8" cy="8" r="7.5" fill="none" stroke="var(--red)"/><rect x="4" y="5.2" width="8" height="5.6" fill="var(--red)"/><path d="M4 5.4l4 3 4-3" fill="none" stroke="var(--white)" stroke-width="0.8"/></svg>
        hello@corvidsystems.com
      </li>
      <li>
        <svg class="contact-icon" viewBox="0 0 16 16"><circle cx="8" cy="8" r="7.5" fill="none" stroke="var(--red)"/><circle cx="8" cy="8" r="4.2" fill="none" stroke="var(--red)" stroke-width="1"/><path d="M3.8 8h8.4M8 3.8v8.4" stroke="var(--red)" stroke-width="0.8"/><ellipse cx="8" cy="8" rx="1.8" ry="4.2" fill="none" stroke="var(--red)" stroke-width="0.8"/></svg>
        www.corvidsystems.com
      </li>
    </ul>
  </div>

  <svg class="wave" viewBox="0 0 560 160" preserveAspectRatio="none">
    <path d="M0 128 C150 120 260 90 360 40 C430 8 500 4 560 2 L560 160 L0 160 Z" fill="var(--red)"/>
    <path d="M0 136 C150 128 262 100 362 50 C432 18 500 14 560 12 L560 160 L0 160 Z" fill="var(--white)"/>
    <path d="M0 140 C150 132 264 104 364 56 C434 24 500 20 560 18 L560 160 L0 160 Z" fill="var(--black)"/>
  </svg>
</section>

</body>
</html>
```